Four IT Graphics for Website

I need four graphics designed to use on my website (https://ovitek.llc) using a white (#ffffff) and orange (#eb4a01) color scheme.

1: Enterprise Architecture Graphic - meet site description of: "Devising strategic blueprints for encompassing the structure, processes, and technology components to harmoniously align your organizations objectives with IT infrastructure, fostering efficiency, agility, and innovation in an ever-evolving digital landscape."

2: CyberSecurity Services - Description "Leveraging the expertise of QRTM certified professionals, our cybersecurity services provide comprehensive, reliable assessments against real-world threats, ensuring your organization's digital assets remain secure in an increasingly vulnerable age."

3: Integrations and Automations - Description "We streamline operations by seamlessly connecting disparate systems, processes, and data, driving increased efficiency, reducing manual tasks, and enabling organizations to unlock new opportunities for growth and innovation."

4: Website Development - Description "Our fully-managed website services comprise every aspect of crafting a visually stunning and highly functional online presence, allowing you to focus on your core business operations while we expertly handle everything from development and site hosting, to boosting your brand recognition."

These will be used on our main and future sub-pages as we continue to expand the website.

I would like the logos to be very similar in design, and style (same theme, if you will,) and just different to meet the service description. Just like a lot of tech services sites use, including:
https://plumvantic.com
https://zimbo.com
https://lomatrix.com/

IT Consulting / Services

IT / CyberSecurity

• Meet primary colors in project description.

```html
<!DOCTYPE html>
<html lang="en">
<head>
<meta charset="utf-8">
<title>Ovitek Networks — Services</title>
<link href="https://fonts.googleapis.com/css2?family=Fira+Sans:wght@700&family=PT+Sans&display=swap" rel="stylesheet">
<style>
  :root {
    --bg: #0d0b12;
    --white: #ffffff;
    --orange: #eb4a01;
    --mark-grey: #d9d9d9;
    --body-grey: #8d8c93;
    --name-grey: #d4d4d4;
  }
  * { margin: 0; padding: 0; box-sizing: border-box; }
  html, body { width: 1200px; height: 1200px; overflow: hidden; background: var(--bg); }
  .canvas { position: relative; width: 1200px; height: 1200px; background: var(--bg); }

  .brand-name {
    position: absolute; top: 186px; left: 0; width: 1200px;
    text-align: center;
    font-family: "Fira Sans", sans-serif; font-weight: 700;
    font-size: 44px; letter-spacing: 1px; line-height: 60px;
    color: var(--name-grey);
  }

  .service { position: absolute; width: 480px; }
  .service-mark { position: absolute; left: 0; top: 0; width: 140px; height: 92px; }
  .service-title {
    position: absolute; top: -2px;
    font-family: "Fira Sans", sans-serif; font-weight: 700;
    font-size: 38px; line-height: 46px; color: var(--white); white-space: nowrap;
  }
  .service-title .accent { display: block; color: var(--orange); }
  .service-text {
    position: absolute; top: 112px; left: 3px; width: 394px;
    font-family: "PT Sans", sans-serif; font-size: 15.4px; line-height: 19.2px;
    color: var(--body-grey); text-align: justify; hyphens: manual;
  }

  .service--architecture { left: 112px; top: 352px; }
  .service--architecture .service-title { left: 166px; }
  .service--security { left: 674px; top: 354px; }
  .service--security .service-title { left: 156px; }
  .service--security .service-text { top: 110px; }
  .service--integration { left: 120px; top: 672px; }
  .service--integration .service-title { left: 168px; }
  .service--integration .service-text { top: 116px; left: -1px; }
  .service--web { left: 672px; top: 672px; }
  .service--web .service-title { left: 165px; }
  .service--web .service-text { top: 116px; left: 5px; }
</style>
</head>
<body>
<main class="canvas">
  <div class="brand-name">OVITEK NETWORKS</div>

  <section class="service service--architecture">
    <svg class="service-mark" viewBox="0 0 140 92" aria-hidden="true">
      <rect x="10" y="6" width="120" height="80" rx="4" fill="var(--mark-grey)"/>
      <polygon points="70,0 116,46 70,92 24,46" fill="var(--orange)"/>
      <rect x="52" y="30" width="12" height="44" fill="var(--white)"/>
      <rect x="66" y="22" width="16" height="52" fill="var(--white)"/>
      <rect x="70" y="28" width="3" height="3" fill="var(--orange)"/>
      <rect x="76" y="28" width="3" height="3" fill="var(--orange)"/>
      <rect x="70" y="36" width="3" height="3" fill="var(--orange)"/>
      <rect x="76" y="36" width="3" height="3" fill="var(--orange)"/>
      <rect x="70" y="44" width="3" height="3" fill="var(--orange)"/>
      <rect x="76" y="44" width="3" height="3" fill="var(--orange)"/>
    </svg>
    <h2 class="service-title">Enterprise<span class="accent">Architecture</span></h2>
    <p class="service-text">Devising strategic blueprints for encompassing the struc&shy;ture, processes, and technology components to harmoni&shy;ously align your organizations objectives with IT infrastruc&shy;ture, fostering efficiency, agility, and innovation in an ev&shy;er-evolving digital landscape.</p>
  </section>

  <section class="service service--security">
    <svg class="service-mark" viewBox="0 0 140 92" aria-hidden="true">
      <rect x="10" y="6" width="120" height="80" rx="4" fill="var(--mark-grey)"/>
      <polygon points="70,0 116,46 70,92 24,46" fill="var(--orange)"/>
      <path d="M62 44 v-8 a8 8 0 0 1 16 0 v8" fill="none" stroke="var(--white)" stroke-width="4"/>
      <rect x="56" y="42" width="28" height="22" rx="3" fill="var(--white)"/>
      <circle cx="70" cy="51" r="3" fill="var(--orange)"/>
      <rect x="68.8" y="51" width="2.4" height="6" fill="var(--orange)"/>
    </svg>
    <h2 class="service-title">Cybersecurity<span class="accent">Services</span></h2>
    <p class="service-text">Devising strategic blueprints for encompassing the struc&shy;ture, processes, and technology components to harmoni&shy;ously align your organizations objectives with IT infrastruc&shy;ture, fostering efficiency, agility, and innovation in an ev&shy;er-evolving digital landscape.</p>
  </section>

  <section class="service service--integration">
    <svg class="service-mark" viewBox="0 0 140 92" aria-hidden="true">
      <rect x="10" y="6" width="120" height="80" rx="4" fill="var(--mark-grey)"/>
      <polygon points="70,0 116,46 70,92 24,46" fill="var(--orange)"/>
      <circle cx="58" cy="38" r="15" fill="none" stroke="var(--white)" stroke-width="4" stroke-dasharray="5 3"/>
      <circle cx="58" cy="38" r="8" fill="var(--white)"/>
      <circle cx="85" cy="58" r="12" fill="none" stroke="var(--white)" stroke-width="4" stroke-dasharray="4 3"/>
      <circle cx="85" cy="58" r="6" fill="var(--white)"/>
    </svg>
    <h2 class="service-title">Integration and<span class="accent">Automations</span></h2>
    <p class="service-text">Devising strategic blueprints for encompassing the struc&shy;ture, processes, and technology components to harmoni&shy;ously align your organizations objectives with IT infrastruc&shy;ture, fostering efficiency, agility, and innovation in an ev&shy;er-evolving digital landscape.</p>
  </section>

  <section class="service service--web">
    <svg class="service-mark" viewBox="0 0 140 92" aria-hidden="true">
      <rect x="10" y="6" width="120" height="80" rx="4" fill="var(--mark-grey)"/>
      <polygon points="70,0 116,46 70,92 24,46" fill="var(--orange)"/>
      <rect x="50" y="26" width="40" height="32" rx="6" fill="none" stroke="var(--white)" stroke-width="5"/>
      <rect x="67" y="58" width="6" height="8" fill="var(--white)"/>
      <rect x="58" y="66" width="24" height="4" rx="2" fill="var(--white)"/>
    </svg>
    <h2 class="service-title">Website<span class="accent">Development</span></h2>
    <p class="service-text">Devising strategic blueprints for encompassing the struc&shy;ture, processes, and technology components to harmoni&shy;ously align your organizations objectives with IT infrastruc&shy;ture, fostering efficiency, agility, and innovation in an ev&shy;er-evolving digital landscape.</p>
  </section>
</main>
</body>
</html>
```